Plumbing & Heating company

A leaflet containing -

Company name - Brackenfold Plumbing Solutions
logo
Mobile number - 07700 914226
Landline - 01632 870512
Email - Info@brackenfoldplumbing.example.co.uk
website - Brackenfold-plumbing.example.co.uk
Social media logos - pixgram, Chatterly

services we offer

- Boiler replacements (free quote)
- General plumbing & heating
- Tap replacements
- 1st & 2nd
- New builds & Extensions
- Cylinder replcemets

```html
<!DOCTYPE html>
<html lang="en">
<head>
<meta charset="utf-8">
<title>Brackenfold Plumbing Solutions Leaflet</title>
<link href="https://fonts.googleapis.com/css2?family=Oswald:wght@600;700&family=Roboto+Condensed:wght@400;700&display=swap" rel="stylesheet">
<style>
  :root {
    --page: #ffffff;
    --ink-dark: #1c1c1e;
    --ink-black: #111111;
    --white: #ffffff;
    --orange: #f39a2e;
    --red: #e8473f;
    --deep-red: #c9302c;
    --yellow: #f6c84a;
    --blue-light: #35b0f5;
    --blue: #1f74c9;
    --blue-deep: #123c82;
    --navy: #183a8a;
    --silver-light: #f2f2f2;
    --silver: #b9bcc0;
    --silver-dark: #7d8085;
  }
  * { box-sizing: border-box; margin: 0; padding: 0; }
  html, body { width: 1200px; height: 1200px; overflow: hidden; background: var(--page); }
  .leaflet {
    position: absolute; left: 152px; top: 20px; width: 896px; height: 1160px;
    background: linear-gradient(to bottom, var(--ink-dark) 0, var(--ink-dark) 858px, var(--red) 858px, #f07a3c 990px, var(--yellow) 1160px);
    overflow: hidden;
    font-family: "Roboto Condensed", Arial, sans-serif;
  }
  .brand-mark {
    position: absolute; left: 77px; top: 60px; width: 347px; text-align: center;
    color: var(--orange); font-family: "Oswald", sans-serif; font-weight: 700; line-height: 1.05;
  }
  .brand-mark .dot { display: block; width: 46px; height: 46px; border-radius: 50%; background: var(--orange); margin: 0 auto 12px; }
  .brand-mark .name { display: block; font-size: 40px; letter-spacing: 1px; }
  .brand-mark .sub { display: block; font-size: 20px; letter-spacing: 3px; }
  .headline {
    position: absolute; left: 73px; top: 236px; width: 380px;
    font-family: "Oswald", sans-serif; font-weight: 700; text-transform: uppercase; line-height: 1.2;
  }
  .headline span { display: block; font-size: 70px; -webkit-background-clip: text; background-clip: text; color: transparent; }
  .headline .warm { background-image: linear-gradient(90deg, var(--orange), var(--red)); }
  .headline .warm.long { font-size: 58px; }
  .headline .cool { background-image: linear-gradient(to bottom, var(--blue-light), var(--blue-deep)); }
  .pipe-frame {
    position: absolute; border: 7px solid var(--silver); border-radius: 12px;
    box-shadow: inset 0 0 0 2px var(--silver-dark), 0 0 0 2px var(--silver-light);
    overflow: hidden;
  }
  .photo { width: 100%; height: 100%; }
  .photo-cupboard { left: 501px; top: 37px; width: 341px; height: 445px; }
  .photo-cupboard .photo { background: linear-gradient(160deg, #d6a877, #b9875a 55%, #9c7350); }
  .photo-pipework { left: 501px; top: 502px; width: 162px; height: 213px; }
  .photo-pipework .photo { background: linear-gradient(150deg, #b7a48e, #8f7359 60%, #6d665e); }
  .photo-cylinder { left: 681px; top: 502px; width: 163px; height: 213px; }
  .photo-cylinder .photo { background: linear-gradient(150deg, #f1f1ef, #d7d6d2 60%, #a9a8a4); }
  .connector { position: absolute; top: 614px; height: 12px; background: var(--silver); border-top: 2px solid var(--silver-light); border-bottom: 2px solid var(--silver-dark); }
  .about {
    position: absolute; left: 68px; top: 502px; width: 414px; height: 213px;
    background: var(--ink-black); padding: 22px 24px 0 30px;
    border: 6px solid var(--silver); border-radius: 10px;
  }
  .about p { color: var(--white); font-size: 23px; line-height: 29px; }
  .about .assurance {
    margin-top: 10px; padding-top: 6px; border-top: 1px solid #444;
    font-weight: 700; font-size: 18px; line-height: 24px; white-space: nowrap;
    text-transform: uppercase; color: var(--orange);
  }
  .about .assurance b { color: var(--blue-light); }
  .services {
    position: absolute; left: 52px; top: 765px; width: 792px; height: 232px;
    border-radius: 16px;
    background: linear-gradient(to bottom, var(--blue-light), var(--blue) 55%, var(--blue-deep));
    border: 9px solid var(--silver); box-shadow: inset 0 0 0 2px var(--silver-dark), 0 4px 10px rgba(0,0,0,.35);
  }
  .services-tab {
    position: absolute; left: 272px; top: 744px; width: 356px; height: 56px;
    background: var(--deep-red); border-radius: 0 0 20px 20px;
    color: var(--white); font-family: "Oswald", sans-serif; font-weight: 700; font-size: 32px;
    text-align: center; line-height: 56px; text-transform: uppercase;
  }
  .service { position: absolute; color: var(--white); font-weight: 700; font-size: 22px; text-transform: uppercase; line-height: 26px; }
  .service svg { position: absolute; left: -22px; top: 4px; }
  .free-quote {
    display: inline-block; margin-top: 2px; padding: 0 12px; border-radius: 12px;
    background: linear-gradient(90deg, var(--red), var(--yellow)); color: var(--ink-black); font-size: 20px;
  }
  .emergency {
    position: absolute; left: 195px; top: 999px; width: 503px; height: 48px;
    background: var(--ink-black); border-radius: 0 0 26px 26px;
    color: var(--white); font-weight: 700; font-size: 26px; text-align: center; line-height: 48px; text-transform: uppercase;
  }
  .contact { position: absolute; font-weight: 700; color: var(--ink-black); font-size: 22px; display: flex; align-items: center; gap: 8px; white-space: nowrap; }
  .contact.email { font-size: 18px; }
  .contact .icon { width: 26px; height: 26px; border-radius: 50%; background: var(--deep-red); display: flex; align-items: center; justify-content: center; flex: none; }
  .website { position: absolute; left: 470px; top: 1058px; font-weight: 700; font-size: 25px; color: var(--ink-black); white-space: nowrap; }
  .follow { position: absolute; left: 472px; top: 1100px; font-weight: 700; font-size: 14px; display: flex; align-items: center; gap: 6px; color: var(--deep-red); text-transform: uppercase; white-space: nowrap; }
  .follow .dot { width: 14px; height: 14px; border-radius: 50%; background: var(--deep-red); }
  .follow .networks { color: var(--ink-black); text-transform: none; }
  .follow .handle { color: var(--navy); text-transform: none; font-weight: 400; }
</style>
</head>
<body>
<main class="leaflet">
  <div class="brand-mark">
    <span class="dot"></span>
    <span class="name">BRACKENFOLD</span>
    <span class="sub">PLUMBING SOLUTIONS</span>
  </div>

  <h1 class="headline">
    <span class="warm long">Brackenfold</span>
    <span class="warm">Plumbing</span>
    <span class="cool">Solutions</span>
  </h1>

  <div class="pipe-frame photo-cupboard"><div class="photo" role="img" aria-label="Photo of a wooden utility cupboard with a wall-mounted boiler and copper pipework"></div></div>

  <section class="about">
    <p>Brackenfold Plumbing &amp; Heating contractor based in Hampshire and covering Winchester and the surrounding areas.</p>
    <p class="assurance"><b>We are Gas Certified</b> and fully insured.</p>
  </section>

  <div class="connector" style="left:482px;width:22px"></div>
  <div class="connector" style="left:660px;width:24px"></div>

  <div class="pipe-frame photo-pipework"><div class="photo" role="img" aria-label="Photo of copper underfloor pipework being installed between timber joists"></div></div>
  <div class="pipe-frame photo-cylinder"><div class="photo" role="img" aria-label="Photo of a hot water cylinder and boiler installation"></div></div>

  <section class="services"></section>
  <h2 class="services-tab">Services we offer</h2>

  <div class="service" style="left:139px;top:822px">
    <svg width="18" height="18" viewBox="0 0 18 18"><circle cx="9" cy="9" r="8" fill="#f6c84a"/><circle cx="9" cy="9" r="6" fill="#c9302c"/><path d="M6 9l2 2 4-4" stroke="#fff" stroke-width="1.8" fill="none"/></svg>
    Boiler replacements<br><span class="free-quote">Free quote</span>
  </div>
  <div class="service" style="left:139px;top:884px">
    <svg width="18" height="18" viewBox="0 0 18 18"><circle cx="9" cy="9" r="8" fill="#f6c84a"/><circle cx="9" cy="9" r="6" fill="#c9302c"/><path d="M6 9l2 2 4-4" stroke="#fff" stroke-width="1.8" fill="none"/></svg>
    General plumbing &amp; heating
  </div>
  <div class="service" style="left:139px;top:920px">
    <svg width="18" height="18" viewBox="0 0 18 18"><circle cx="9" cy="9" r="8" fill="#f6c84a"/><circle cx="9" cy="9" r="6" fill="#c9302c"/><path d="M6 9l2 2 4-4" stroke="#fff" stroke-width="1.8" fill="none"/></svg>
    Tap replacements
  </div>
  <div class="service" style="left:479px;top:822px">
    <svg width="18" height="18" viewBox="0 0 18 18"><circle cx="9" cy="9" r="8" fill="#f6c84a"/><circle cx="9" cy="9" r="6" fill="#c9302c"/><path d="M6 9l2 2 4-4" stroke="#fff" stroke-width="1.8" fill="none"/></svg>
    System design &amp; installation<br>-1st &amp; 2nd fix
  </div>
  <div class="service" style="left:479px;top:884px">
    <svg width="18" height="18" viewBox="0 0 18 18"><circle cx="9" cy="9" r="8" fill="#f6c84a"/><circle cx="9" cy="9" r="6" fill="#c9302c"/><path d="M6 9l2 2 4-4" stroke="#fff" stroke-width="1.8" fill="none"/></svg>
    New builds &amp; extensions
  </div>
  <div class="service" style="left:479px;top:920px">
    <svg width="18" height="18" viewBox="0 0 18 18"><circle cx="9" cy="9" r="8" fill="#f6c84a"/><circle cx="9" cy="9" r="6" fill="#c9302c"/><path d="M6 9l2 2 4-4" stroke="#fff" stroke-width="1.8" fill="none"/></svg>
    Cylinder replcemets
  </div>

  <p class="emergency">Emergency call outs available</p>

  <div class="contact" style="left:71px;top:1062px">
    <span class="icon"><svg width="12" height="16" viewBox="0 0 12 16"><rect x="1.5" y="1" width="9" height="14" rx="1.5" fill="none" stroke="#fff" stroke-width="1.6"/></svg></span>07700 914226
  </div>
  <div class="contact" style="left:252px;top:1062px">
    <span class="icon"><svg width="16" height="12" viewBox="0 0 16 12"><path d="M1 4c4-4 10-4 14 0l-2 2-2-1V3H5v2L3 6z" fill="#fff"/><rect x="4" y="7" width="8" height="4" rx="1" fill="#fff"/></svg></span>01632 870512
  </div>
  <div class="contact email" style="left:71px;top:1098px">
    <span class="icon"><svg width="14" height="10" viewBox="0 0 14 10"><rect x="0.8" y="0.8" width="12.4" height="8.4" fill="none" stroke="#fff" stroke-width="1.4"/><path d="M1 1l6 5 6-5" fill="none" stroke="#fff" stroke-width="1.4"/></svg></span>Info@brackenfoldplumbing.example.co.uk
  </div>

  <p class="website">Brackenfold-plumbing.example.co.uk</p>
  <p class="follow"><span class="dot"></span><span class="networks">Chatterly · pixgram</span> Follow us: <span class="handle">Brackenfoldplumbingsolutions</span></p>
</main>
</body>
</html>
```